IT services company requires Letterhead design

We need a professional letterhead designed to be used for general correspondence with customers, quotes, invoices etc. We are a new IT services company specialising in computer servicing and repairs and mobile and tablet repairs. Attached are templates that my printing company have supplied, my logos, an interpretation of our website for you to get a feel of the company. Details to be included on the letterhead are

Company Number – 4738261
VAT Number - 518337942
Registered Address – 14-16 Brambly Lane, London, E4 9QT

Phone – 01632 487215
Email – sales@quorvent.com
Web – www.quorvent.com

I would prefer for the top of the letterhead to just have the company logo on a white background and the rest of the details on the bottom of the letterhead but I am open to design ideas.

Thanks

```html
<!DOCTYPE html>
<html lang="en">
<head>
<meta charset="utf-8">
<title>Quorvent Letterhead</title>
<link rel="stylesheet" href="https://fonts.googleapis.com/css2?family=Carlito:wght@400;700&family=Ubuntu:wght@400;500;700&display=swap">
<style>
  :root {
    --brand: #31c0e3;
    --ink: #4a4a4a;
    --ink-soft: #555;
    --paper: #ffffff;
    --mark: #f2f2f2;
  }
  * { margin: 0; padding: 0; box-sizing: border-box; }
  html, body { width: 864px; height: 1200px; overflow: hidden; background: var(--paper); }
  .letterhead {
    position: relative; width: 864px; height: 1200px; background: var(--paper);
    font-family: "Carlito", "Calibri", sans-serif; color: var(--ink);
  }
  .header-band { position: absolute; left: 0; top: 0; width: 864px; height: 78px; background: var(--brand); }
  .brand-plate {
    position: absolute; left: 523px; top: 18px; width: 261px; height: 128px;
    background: linear-gradient(to bottom, #fff 0, #fff 60px, rgba(250,250,250,0.6) 100%);
    display: flex; justify-content: center; padding-top: 6px;
  }
  .brand-name {
    font-family: "Ubuntu", sans-serif; font-weight: 700; font-size: 42px;
    color: var(--brand); letter-spacing: 0.5px; line-height: 48px;
  }
  .backdrop-name {
    position: absolute; left: 230px; top: 520px; transform: rotate(-30deg);
    font-family: "Ubuntu", sans-serif; font-weight: 700; font-size: 150px;
    color: var(--mark); line-height: 1; white-space: nowrap; pointer-events: none;
  }
  .recipient {
    position: absolute; left: 60px; top: 282px;
    font-family: "Ubuntu", sans-serif; font-size: 14.5px; line-height: 28px; color: var(--ink-soft);
  }
  .recipient .name { font-weight: 500; color: var(--ink); }
  .salutation {
    position: absolute; left: 60px; top: 454px;
    font-family: "Ubuntu", sans-serif; font-weight: 500; font-size: 17.5px; color: var(--ink);
  }
  .body-copy { position: absolute; left: 60px; top: 510px; width: 730px; font-size: 14px; }
  .body-copy p { line-height: 30.5px; margin-bottom: 8px; }
  .body-copy p + p + p { margin-top: 4px; }
  .body-copy span { display: block; white-space: nowrap; }
  .closing-right {
    position: absolute; right: 78px; top: 912px;
    font-family: "Ubuntu", sans-serif; font-size: 14.5px; color: var(--ink-soft);
  }
  .sign-off {
    position: absolute; left: 60px; top: 932px;
    font-family: "Ubuntu", sans-serif; font-size: 14.5px; line-height: 26px; color: var(--ink-soft);
  }
  .sign-off .first { margin-bottom: 3px; }
  .footer-band {
    position: absolute; left: 0; top: 1117px; width: 864px; height: 83px; background: var(--brand);
    color: #fff; font-size: 11.5px;
  }
  .company-details { position: absolute; right: 451px; top: 12px; text-align: right; line-height: 16.5px; }
  .footer-divider { position: absolute; left: 430px; top: 12px; width: 1px; height: 52px; background: rgba(255,255,255,0.6); }
  .contact-details { position: absolute; left: 451px; top: 12px; line-height: 18px; list-style: none; }
  .contact-details li { display: flex; align-items: center; gap: 7px; }
  .contact-details svg { width: 10px; height: 10px; fill: #fff; flex: none; }
</style>
</head>
<body>
<main class="letterhead">
  <div class="header-band"></div>
  <div class="brand-plate"><span class="brand-name">Quorvent</span></div>

  <div class="backdrop-name" aria-hidden="true">Quorvent</div>

  <address class="recipient" style="font-style:normal">
    <div class="name">John Smith</div>
    <div>Owner</div>
    <div>Company Name</div>
    <div>Address Line1, Address Line2</div>
    <div>Country -123456</div>
  </address>

  <h2 class="salutation">Dear John Smith</h2>

  <section class="body-copy">
    <p>
      <span>Lorem ipsum dolor sit amet, consectetur adipiscing elit, sed do eiusmod tempor incididunt ut labore et dolore magna</span>
      <span>aliqua. Ut enim ad minim veniam, quis nostrud exercitation ullamco laboris nisi ut aliquip ex ea commodo consequat.</span>
      <span>Duis aute irure dolor in reprehenderit in voluptate velit esse cillum dolore eu fugiat nulla pariatur. Excepteur sint occa</span>
      <span>ecat cupidatat non proident, sunt in culpa qui officia deserunt mollit anim id est laborum.</span>
    </p>
    <p>
      <span>Lorem ipsum dolor sit amet, consectetur adipiscing elit, sed do eiusmod tempor incididunt ut labore et dolore magna</span>
      <span>aliqua. Ut enim ad minim veniam, quis nostrud exercitation ullamco laboris nisi ut aliquip ex ea commodo consequat.</span>
      <span>Duis aute irure dolor in reprehenderit in voluptate velit esse cillum dolore eu fugiat nulla pariatur. Excepteur sint occa</span>
      <span>ecat cupidatat non proident, sunt in culpa qui officia deserunt mollit anim id est laborum.</span>
    </p>
    <p>
      <span>Lorem ipsum dolor sit amet, consectetur adipiscing elit, sed do eiusmod tempor incididunt ut labore et dolore magna</span>
      <span>aliqua. Ut enim ad minim veniam, quis nostrud exercitation ullamco laboris nisi ut aliquip ex ea commodo consequat.</span>
      <span>Duis aute irure dolor in reprehenderit in voluptate velit esse cillum dolore eu fugiat nulla pariatur. Excepteur sint occa</span>
      <span>ecat cupidatat non proident, sunt in culpa qui officia deserunt mollit anim id est laborum.</span>
    </p>
  </section>

  <div class="closing-right">Your Faithfully</div>
  <div class="sign-off">
    <div class="first">Sincerely</div>
    <div>[Title]</div>
    <div>[Your Name]</div>
  </div>

  <footer class="footer-band">
    <div class="company-details">
      <div>4738261 - Company Number</div>
      <div>518337942 - VAT Number</div>
      <div>14-16 Brambly Lane, London, E4 9QT - Address</div>
    </div>
    <div class="footer-divider"></div>
    <ul class="contact-details">
      <li><svg viewBox="0 0 10 10"><path d="M2.2 0.5 L3.6 2.6 L2.8 3.6 Q3.6 5.6 5.9 6.9 L6.9 6.1 L9 7.5 L8 9.3 Q2 8.5 0.6 1.5 Z"/></svg>01632 487215</li>
      <li><svg viewBox="0 0 10 10"><path d="M0.5 2 H9.5 V8.2 H0.5 Z M1.2 2.6 L5 5.4 L8.8 2.6" stroke="#31c0e3" stroke-width="0.8"/></svg>sales@quorvent.com</li>
      <li><svg viewBox="0 0 10 10" fill="none"><g stroke="#fff" stroke-width="0.9" fill="none"><circle cx="5" cy="5" r="4.3"/><ellipse cx="5" cy="5" rx="1.9" ry="4.3"/><path d="M0.7 5 H9.3 M1.4 2.8 H8.6 M1.4 7.2 H8.6"/></g></svg>www.quorvent.com</li>
    </ul>
  </footer>
</main>
</body>
</html>
```